Wordpress website design for Tavi Linkway-Africa

We need a website for a new consultancy and digital marketplace in Kenya called 'Tavi Linkway - Africa'. Please refer to the the attached document [Tavi Linkway Africa website brief] and contact me anytime.

Bests,
Philippa

Deadline extended to allow for additional revisions and refinements, ensuring that final designs align closely with project objectives and quality standards. This extra time will help incorporate valuable feedback and ensure the final output meets our high expectations.

```html
<!DOCTYPE html>
<html lang="en">
<head>
<meta charset="utf-8">
<title>Tavi Linkway - Africa</title>
<link href="https://fonts.googleapis.com/css2?family=Poppins:wght@400;500;600;700&display=swap" rel="stylesheet">
<style>
:root{
  --navy:#1f3d5f;
  --navy-deep:#1a3553;
  --green:#4cbc63;
  --ink:#1f3d5f;
  --text:#4a5565;
  --muted:#7d8794;
  --light:#f4f5f6;
  --white:#ffffff;
}
*{box-sizing:border-box;margin:0;padding:0}
html,body{width:1200px;height:4508px;overflow:hidden}
body{position:relative;font-family:"Poppins",sans-serif;color:var(--text);background:var(--white)}
.abs{position:absolute}
.btn-outline{position:absolute;border:1.5px solid var(--green);color:var(--green);font-size:9px;font-weight:500;display:flex;align-items:center;justify-content:center;border-radius:2px;background:var(--white)}
.btn-solid{position:absolute;background:var(--green);color:var(--white);font-size:9px;font-weight:500;display:flex;align-items:center;justify-content:center;border-radius:2px}
.section-title{position:absolute;left:0;width:1200px;text-align:center;color:var(--ink);font-weight:600;font-size:24px}

/* hero */
.hero{position:absolute;left:0;top:0;width:1200px;height:574px;background:var(--light)}
.hero-photo{position:absolute;left:600px;top:0;width:600px;height:574px;background:linear-gradient(135deg,#6b4a3a,#3b3a3f 45%,#8a8f96)}
.brand{position:absolute;display:flex;align-items:center;gap:8px;color:var(--navy);font-weight:600;white-space:nowrap}
.brand .dot{width:24px;height:24px;border-radius:50%;background:var(--green);flex:none}
.nav{position:absolute;left:385px;top:21px;width:432px;height:40px;background:var(--white);display:flex;align-items:center;font-size:9px;color:var(--navy)}
.nav span{position:absolute;white-space:nowrap}
.hero h1{position:absolute;left:107px;top:166px;font-size:46px;line-height:56px;color:var(--ink);font-weight:600}
.hero p{position:absolute;left:107px;top:360px;width:360px;font-size:13px;line-height:19px;color:var(--navy)}

/* services */
.services-band{position:absolute;left:0;top:1271px;width:1200px;height:312px;background:var(--navy)}
.service{position:absolute;top:1240px;width:300px;height:373px;text-align:center;color:var(--white)}
.service h3{position:absolute;top:154px;left:0;width:300px;font-size:13px;font-weight:500;line-height:18px}
.service p{position:absolute;top:190px;left:40px;width:220px;font-size:8.5px;line-height:14px;opacity:.85}
.service .btn{position:absolute;top:255px;left:100px;width:100px;height:28px;border:1px solid rgba(255,255,255,.7);font-size:8px;display:flex;align-items:center;justify-content:center}
.service svg{position:absolute;top:89px;left:130px}

/* products */
.card{position:absolute;top:2146px;width:248px;height:290px;background:var(--white);box-shadow:0 4px 16px rgba(0,0,0,.08)}
.card .img{height:140px;background:linear-gradient(160deg,#c9a27a,#b58659 55%,#d9d4cc)}
.card .tag{position:absolute;left:8px;top:8px;font-size:6px;color:var(--white);background:#7ab890;padding:2px 6px;border-radius:6px}
.card h4{position:absolute;left:18px;top:156px;font-size:11px;color:var(--ink);font-weight:500}
.card p{position:absolute;left:18px;top:182px;width:200px;font-size:8px;line-height:12px;color:var(--muted)}
.card .stars{position:absolute;left:18px;top:228px;font-size:8px;color:#f1b52b}
.card .stars small{color:var(--muted);font-size:6px;margin-left:4px}
.card .price{position:absolute;left:0;top:254px;width:62px;height:22px;background:var(--navy);color:var(--white);font-size:10px;font-weight:600;border-radius:0 11px 11px 0;padding-left:18px;line-height:22px}
.card .buy{position:absolute;right:18px;top:258px;font-size:8px;color:var(--green);text-decoration:underline}

/* team */
.team{position:absolute;left:0;top:2583px;width:1200px;height:478px;background:var(--green)}
.member{position:absolute;top:137px;width:180px;text-align:center;color:var(--white)}
.member .avatar{width:112px;height:112px;border-radius:50%;margin:0 auto;background:linear-gradient(160deg,#e8d7c6,#b88e6e);border:3px solid var(--white)}
.member h5{font-size:12px;font-weight:500;margin-top:12px}
.member small{display:block;font-size:8px;margin-top:2px;opacity:.9}
.member .in{width:24px;height:24px;border:1px solid var(--white);border-radius:50%;margin:12px auto 0;font-size:8px;line-height:22px}

/* articles */
.article-date{position:absolute;font-size:8px;color:var(--green)}
.article-title{position:absolute;font-size:12px;line-height:18px;color:var(--ink);width:200px}
.article-arrow{position:absolute;font-size:10px;color:var(--green)}

/* consult */
.consult{position:absolute;left:0;top:3760px;width:1200px;height:408px;background:var(--light)}
.field{position:absolute;left:614px;display:flex;align-items:baseline;gap:14px;border-bottom:1px solid #d9dde2;padding-bottom:6px}
.field label{font-size:16px;color:var(--ink);font-weight:500}
.field span{font-size:12px;color:var(--muted)}

/* footer */
.footer{position:absolute;left:0;top:4168px;width:1200px;height:340px;background:var(--navy)}
.footer h6{position:absolute;font-size:13px;color:var(--white);font-weight:500}
.footer .line{position:absolute;font-size:10px;color:#d6dde6}
.social{position:absolute;top:4326px;width:26px;height:26px;border-radius:50%;background:rgba(255,255,255,.18)}
</style>
</head>
<body>

<!-- HERO -->
<section class="hero">
  <div class="hero-photo" role="img" aria-label="Photo of consultants in discussion around a laptop in an office"></div>
  <div class="brand" style="left:108px;top:30px;font-size:17px"><span class="dot"></span>TAVI LINKWAY</div>
  <nav class="nav">
    <span style="left:33px;color:var(--green)">Home</span>
    <span style="left:91px">Services</span>
    <span style="left:138px">Digital Marketplace</span>
    <span style="left:248px">About Us</span>
    <span style="left:315px">Blog</span>
    <span style="left:361px">Contact Us</span>
  </nav>
  <div class="abs" style="left:892px;top:36px;font-size:9px;color:var(--white)">&#9990; 555-210-4471</div>
  <div class="btn-solid" style="left:993px;top:28px;width:100px;height:30px">Consult now!</div>
  <h1>Digital,<br>technology &amp;<br>data</h1>
  <p>Empowering innovations &amp; digital transformation across africa.</p>
  <div class="abs" style="left:106px;top:431px;width:36px;height:36px;border-radius:50%;background:var(--green)"></div>
  <svg class="abs" style="left:115px;top:440px" width="18" height="18" viewBox="0 0 18 18"><circle cx="9" cy="9" r="6" fill="none" stroke="#fff" stroke-width="1.5"/><circle cx="9" cy="9" r="2" fill="#fff"/></svg>
  <div class="abs" style="left:152px;top:443px;font-size:9px;color:var(--green);font-weight:500">Discover tavi</div>
  <div class="abs" style="left:574px;top:548px;width:26px;height:26px;background:var(--white);color:var(--muted);font-size:10px;text-align:center;line-height:26px">&larr;</div>
  <div class="abs" style="left:600px;top:548px;width:26px;height:26px;background:#2c6fb0;color:var(--white);font-size:10px;text-align:center;line-height:26px">&rarr;</div>
</section>

<!-- ABOUT -->
<section>
  <div class="abs" style="left:268px;top:649px;width:283px;height:334px;border:1.5px solid #c7ccd3"></div>
  <div class="abs" role="img" aria-label="Photo of a family working together at a laptop" style="left:201px;top:665px;width:331px;height:376px;background:linear-gradient(150deg,#e6e2dc,#7e6a58 55%,#c9c2b8)"></div>
  <div class="abs" style="left:612px;top:716px;font-size:9px;color:var(--green);font-weight:500">Welcome to Tavi Linkway</div>
  <h2 class="abs" style="left:612px;top:748px;width:395px;font-size:19px;line-height:26px;color:var(--ink);font-weight:600">Tavi Linkway africa is a consultancy firm and digital marketplace dedicated to supporting africa’s digital transformation.</h2>
  <p class="abs" style="left:612px;top:874px;width:395px;font-size:8.5px;line-height:14px;color:var(--muted)">We provide data-driven insights, strategic guidance, customised solutions to empower public and private sectors. We aim to tackle complex challenges, optimize operations, and unlock growth through innovative technology...</p>
  <div class="btn-outline" style="left:612px;top:944px;width:100px;height:28px">About us</div>
</section>

<!-- WHAT WE DO -->
<div class="abs" style="left:107px;top:1114px;width:986px;height:156px;background:var(--light)"></div>
<div class="section-title" style="top:1158px">What We Do</div>
<div class="services-band"></div>
<div class="abs" style="left:900px;top:1271px;width:1px;height:312px;background:rgba(255,255,255,.1)"></div>

<div class="service" style="left:0">
  <svg width="40" height="48" viewBox="0 0 40 48"><path d="M10 44h22M13 38h16l-2-12 6-6-6-12-10 4-6 12 8 2-6 12z" fill="none" stroke="#4cbc63" stroke-width="2"/></svg>
  <h3>Digital Strategy</h3>
  <p>It is a long established fact that a reader will be distracted by the readable content of a when looking at its layout...</p>
  <div class="btn">Learn More</div>
</div>
<div class="service" style="left:300px;background:linear-gradient(180deg,#5d6d7c,#415a74 60%,#2f4a69)" role="img" aria-label="Photo of a team working on laptops">
  <svg width="40" height="48" viewBox="0 0 40 48"><circle cx="20" cy="16" r="9" fill="none" stroke="#fff" stroke-width="2"/><path d="M6 44c2-10 8-14 14-14s12 4 14 14z" fill="none" stroke="#fff" stroke-width="2"/></svg>
  <h3>Technical Expertise</h3>
  <p>It is a long established fact that a reader will be distracted by the readable content of a when looking at its layout...</p>
  <div class="btn" style="background:var(--green);border-color:var(--green)">Learn More</div>
</div>
<div class="service" style="left:600px">
  <svg width="40" height="48" viewBox="0 0 40 48"><rect x="6" y="4" width="24" height="36" fill="none" stroke="#fff" stroke-width="2"/><path d="M12 30v-8M18 30v-12M24 30v-5" stroke="#4cbc63" stroke-width="2"/><circle cx="28" cy="36" r="6" fill="none" stroke="#fff" stroke-width="2"/></svg>
  <h3>Data Analytics</h3>
  <p>It is a long established fact that a reader will be distracted by the readable content of a when looking at its layout...</p>
  <div class="btn">Learn More</div>
</div>
<div class="service" style="left:900px">
  <svg width="40" height="48" viewBox="0 0 40 48"><rect x="10" y="14" width="20" height="20" fill="none" stroke="#fff" stroke-width="2"/><path d="M14 8v6M20 8v6M26 8v6M14 34v6M20 34v6M26 34v6M4 20h6M4 28h6M30 20h6M30 28h6" stroke="#fff" stroke-width="2"/><text x="20" y="28" font-size="8" fill="#fff" text-anchor="middle" font-family="Poppins,sans-serif">AI</text></svg>
  <h3 style="top:146px">Artificial Intelligence &amp;<br>Machine Learning</h3>
  <p>It is a long established fact that a reader will be distracted by the readable content of a when looking at its layout...</p>
  <div class="btn">Learn More</div>
</div>

<!-- E-COMMERCE -->
<section class="abs" style="left:0;top:1613px;width:1200px;height:399px;background:var(--light)"></section>
<h2 class="abs" style="left:201px;top:1690px;font-size:38px;line-height:50px;color:var(--ink);font-weight:600">e-Commerce<br>for Digital Products</h2>
<p class="abs" style="left:201px;top:1812px;width:460px;font-size:13px;line-height:21px;color:var(--navy)">Lorem Ipsum is simply dummy text of the printing and typesetting industry lorem Ipsum has been the industry's standard dummy text ever since.</p>
<div class="btn-solid" style="left:201px;top:1908px;width:135px;height:28px">Explore digital products</div>
<div class="abs" role="img" aria-label="Collage of digital product imagery" style="left:756px;top:1690px;width:188px;height:246px;border-radius:14px;background:linear-gradient(160deg,#d9e8dc,#b8c3d4 50%,#e6d2cc)"></div>

<!-- FEATURED PRODUCTS -->
<div class="section-title" style="top:2082px">Featured Products</div>
<div class="card" style="left:201px"><div class="img" role="img" aria-label="Photo of a laptop on a wooden desk"></div><span class="tag">Skills</span><h4>Contrary Popular Belief</h4><p>There are many variations of passages of lorem ipsum available, but the majority have suffered alteration.</p><div class="stars">★★★★★<small>20 reviews</small></div><div class="price">$27</div><span class="buy">Buy now!</span></div>
<div class="card" style="left:476px"><div class="img" role="img" aria-label="Photo of a laptop on a wooden desk"></div><span class="tag">Strategy</span><h4>Contrary Popular Belief</h4><p>There are many variations of passages of lorem ipsum available, but the majority have suffered alteration.</p><div class="stars">★★★★★<small>20 reviews</small></div><div class="price">$27</div><span class="buy">Buy now!</span></div>
<div class="card" style="left:750px"><div class="img" role="img" aria-label="Photo of a laptop on a wooden desk"></div><span class="tag">Skills</span><h4>Contrary Popular Belief</h4><p>There are many variations of passages of lorem ipsum available, but the majority have suffered alteration.</p><div class="stars">★★★★★<small>20 reviews</small></div><div class="price">$27</div><span class="buy">Buy now!</span></div>
<div class="btn-outline" style="left:551px;top:2478px;width:100px;height:30px">View all</div>

<!-- TEAM -->
<section class="team">
  <div class="section-title" style="top:67px;color:var(--white)">Meet The Team</div>
  <div class="abs" style="left:168px;top:180px;color:var(--white);font-size:22px">&#8249;</div>
  <div class="abs" style="left:1016px;top:180px;color:var(--white);font-size:22px">&#8250;</div>
  <div class="member" style="left:200px"><div class="avatar" role="img" aria-label="Portrait of a team member"></div><h5>J. Maren</h5><small>Contrary to popular belief</small><div class="in">in</div></div>
  <div class="member" style="left:407px"><div class="avatar" role="img" aria-label="Portrait of a team member"></div><h5>Olu Dayo</h5><small>Contrary to popular belief</small><div class="in">in</div></div>
  <div class="member" style="left:613px"><div class="avatar" role="img" aria-label="Portrait of a team member"></div><h5>J. Maren</h5><small>Contrary to popular belief</small><div class="in">in</div></div>
  <div class="member" style="left:820px"><div class="avatar" role="img" aria-label="Portrait of a team member"></div><h5>Olu Dayo</h5><small>Contrary to popular belief</small><div class="in">in</div></div>
  <div class="abs" style="left:551px;top:373px;width:100px;height:30px;background:var(--white);color:var(--green);font-size:9px;font-weight:500;display:flex;align-items:center;justify-content:center">View all</div>
</section>

<!-- ARTICLES -->
<h2 class="abs" style="left:275px;top:3146px;font-size:24px;color:var(--ink);font-weight:600">Latest Articles</h2>
<div class="abs" role="img" aria-label="Photo of hands typing on a laptop showing dashboards" style="left:275px;top:3227px;width:313px;height:283px;background:linear-gradient(150deg,#dfe6ea,#a9bfc9 50%,#e7c45a)"></div>
<div class="article-date" style="left:294px;top:3525px">03/11/2024</div>
<div class="article-title" style="left:294px;top:3546px">Lorem ipsum simply dummy printing typesetting</div>
<div class="article-arrow" style="left:294px;top:3588px">&rarr;</div>
<div class="btn-outline" style="left:275px;top:3657px;width:99px;height:29px">View all news</div>

<div class="abs" role="img" aria-label="Photo of a woman celebrating among city towers" style="left:612px;top:3136px;width:311px;height:166px;background:linear-gradient(170deg,#e8ecef,#9aa3ad 60%,#6b6f72)"></div>
<div class="article-date" style="left:632px;top:3316px">10/11/2024</div>
<div class="article-title" style="left:632px;top:3337px">Lorem ipsum simply dummy printing typesetting</div>
<div class="article-arrow" style="left:632px;top:3378px">&rarr;</div>

<div class="abs" role="img" aria-label="Photo of two colleagues discussing documents" style="left:612px;top:3419px;width:311px;height:171px;background:linear-gradient(160deg,#d7d3cd,#6c5849 55%,#bfb7ad)"></div>
<div class="article-date" style="left:632px;top:3600px">14/11/2024</div>
<div class="article-title" style="left:632px;top:3621px">Lorem ipsum simply dummy printing typesetting</div>
<div class="article-arrow" style="left:632px;top:3662px">&rarr;</div>

<!-- CONSULT -->
<section class="consult">
  <h2 class="abs" style="left:201px;top:140px;font-size:38px;color:var(--ink);font-weight:600">Consult Now!</h2>
  <p class="abs" style="left:201px;top:206px;width:360px;font-size:22px;line-height:30px;color:var(--navy)">Send your request and we will contact you!</p>
</section>
<div class="field" style="top:3842px;width:353px"><label>Hi! I am</label><span>eg. Andy lorem</span></div>
<div class="field" style="top:3898px;width:380px"><label>Reach me at</label><span>example@mailbox.com</span></div>
<div class="field" style="top:3954px;width:340px"><label>Phone</label><span>Xxx-xxx-xxxx</span></div>
<div class="field" style="top:4010px;width:380px"><label>Comments</label><span>type your message...</span></div>
<div class="btn-solid" style="left:614px;top:4061px;width:98px;height:30px">Submit</div>

<!-- FOOTER -->
<footer class="footer">
  <div class="brand" style="left:201px;top:80px;font-size:27px;color:var(--white)"><span class="dot" style="width:40px;height:40px"></span>TAVI LINKWAY</div>
  <h6 style="left:528px;top:64px">Contact Us</h6>
  <div class="line" style="left:528px;top:100px;font-size:14px;color:var(--white)"><span style="color:var(--green)">&#9990;</span> 555.018.2245</div>
  <div class="line" style="left:528px;top:132px"><span style="color:var(--green)">&#9993;</span> info@tavilinkway.com</div>
  <div class="line" style="left:528px;top:160px;line-height:22px"><span style="color:var(--green)">&#9679;</span> 18 Kito Lane, # Ipsum,<br>&nbsp;&nbsp;&nbsp;&nbsp;MH 40117</div>
  <h6 style="left:763px;top:64px">Quick links</h6>
  <div class="line" style="left:763px;top:101px;line-height:22.5px">Home<br>Services<br>Digital marketplace<br>About us<br>Blog</div>
  <div class="line" style="left:885px;top:101px;line-height:22.5px">Contact us<br>Terms and conditions<br>Privacy policy</div>
  <div class="line" style="left:201px;top:274px;font-size:9px">© 2024 <span style="color:var(--green)">Tavi Linkway</span> - All Rights Reserved</div>
  <svg class="abs" style="left:1084px;top:268px" width="18" height="20" viewBox="0 0 18 20"><path d="M9 2L16 18L9 14L2 18Z" fill="#4cbc63"/></svg>
</footer>
<div class="social" style="left:263px"></div>
<div class="social" style="left:300px;background:var(--green)"></div>
<div class="social" style="left:337px"></div>
<div class="social" style="left:375px"></div>

</body>
</html>
```